Business card design needed

I have started a new business called Marlow Auto Electrical, although the words Marlow Auto Electrical will be used on signage and documents I actually want to market the business as MAE. The services I offer are Mobile Auto Electrical, Automotive Air Conditioning and Test And Tag. My business will be targetting the Mining Industry, Civil, Rail, Agricultural and Workshop Testing And Tagging. My auto electrical service ranges from fault finding to new vehicle and mine compliance fit outs. I have a very strong focus on quality workmanship. I will upload the logo I have designed and want to use I am happy for the logo colour to change but the design itself must stay the same. I want the design to have a modern, eye catching, energetic feel. As I am a passionate motorsport fan I am happy for this to also influence the design. I am happy for the front of the card to have only the emblem and logo design and the back to have all the info.

Industry/Entity Type

Electrical

Contact Information for Business Card

MAE Marlow Auto Electrical, Glen Tavish, Auto Electrician, Mobile No 0417268354

Requirements
Must have
• On the business card it is mandatory that the following license numbers are shown:

MVRL83742
PXB L731406
ABN 48 913 260 154

```html
<!DOCTYPE html>
<html lang="en">
<head>
<meta charset="utf-8">
<title>MAE Marlow Auto Electrical – Business Card</title>
<link rel="stylesheet" href="https://fonts.googleapis.com/css2?family=Tinos&display=swap">
<style>
  :root {
    --card-edge: #0e0f10;
    --card-mid: #1c1e20;
    --card-glow: #2a2d30;
    --ink-light: #f4f4f4;
    --rule-light: #ffffff;
  }
  * { margin: 0; padding: 0; box-sizing: border-box; }
  html, body {
    width: 691px;
    height: 1200px;
    overflow: hidden;
    background: var(--card-edge);
  }
  .business-card {
    position: relative;
    width: 691px;
    height: 1200px;
    overflow: hidden;
    font-family: "Tinos", "Times New Roman", serif;
    font-weight: 400;
    color: var(--ink-light);
  }
  .card-texture {
    position: absolute;
    inset: 0;
    background:
      radial-gradient(ellipse 85% 45% at 50% 30%, rgba(60, 64, 68, 0.55) 0%, rgba(60, 64, 68, 0) 70%),
      linear-gradient(160deg, var(--card-mid) 0%, var(--card-glow) 35%, var(--card-mid) 70%, var(--card-edge) 100%);
  }
  .brand-lockup {
    position: absolute;
    top: 150px;
    left: 0;
    width: 100%;
    text-align: center;
    color: var(--ink-light);
  }
  .brand-initials {
    display: block;
    font-size: 176px;
    line-height: 176px;
    letter-spacing: 4px;
  }
  .brand-name {
    display: block;
    margin-top: 4px;
    font-size: 31px;
    line-height: 36px;
    letter-spacing: 1.5px;
  }
  .licence-list {
    position: absolute;
    top: 925px;
    left: 0;
    width: 100%;
    text-align: center;
    font-size: 25px;
    line-height: 32.5px;
  }
  .divider {
    position: absolute;
    top: 1045px;
    left: 143px;
    width: 406px;
    height: 4px;
  }
  .contact-details {
    position: absolute;
    top: 1072px;
    left: 0;
    width: 100%;
    text-align: center;
    font-size: 25px;
    line-height: 32.5px;
  }
</style>
</head>
<body>
  <main class="business-card">
    <div class="card-texture" role="img" aria-label="Dark carbon fibre texture background"></div>

    <h1 class="brand-lockup">
      <span class="brand-initials">MAE</span>
      <span class="brand-name">Marlow Auto Electrical</span>
    </h1>

    <div class="licence-list">
      <p>MVRL83742</p>
      <p>PXB L731406</p>
      <p>ABN 48 913 260 154</p>
    </div>

    <svg class="divider" viewBox="0 0 406 4" aria-hidden="true">
      <defs>
        <linearGradient id="rule-fade" x1="0" x2="1" y1="0" y2="0">
          <stop offset="0" stop-color="var(--rule-light)" stop-opacity="0"/>
          <stop offset="0.15" stop-color="var(--rule-light)" stop-opacity="0.95"/>
          <stop offset="0.85" stop-color="var(--rule-light)" stop-opacity="0.95"/>
          <stop offset="1" stop-color="var(--rule-light)" stop-opacity="0"/>
        </linearGradient>
      </defs>
      <path d="M0 2 Q203 -0.5 406 2 Q203 4.5 0 2 Z" fill="url(#rule-fade)"/>
    </svg>

    <div class="contact-details">
      <p>MAE Marlow Auto Electrical,</p>
      <p>Glen Tavish, Auto Electrician,</p>
      <p>Mobile No 0417268354</p>
    </div>
  </main>
</body>
</html>
```